VOLT - Monitoring Natural Hazards from Space Web Application

KORMEL Sarl is a Luxembourg based Space-Startup that works in the field of Earth Observation. KORMEL is a platform able to extract value-added information from satellite data and is specialized in mapping Natural Disaster (floods, fires etc).

We are now developing a new vertical tool, called VOLT, dedicated to the monitoring of natural hazards in Humanitarian Camps around the world.

The goal of VOLT is to hide to the users' all the complexity of the Satellite Image processing and just provide them the results.

This project require to Design 4 pages of VOLT:
• Public Home Page (Code - V01)
• Dashboard (private Home Page) (Code - V03)
• Monitor (web GIS) (Code - V14)
• Registration Page (Code - V04)

We would like to provide the required time to make a good job.

Target Market(s)

Humanitarian Agencies, Goverments

Coding

Coded - Design and coding required

Number of Pages Required

4 page

Font styles to use
Other font styles liked:
• see the manual attached

Requirements
Must have
• 4 pages. One Home, one form, one dashboard and one web map.
Nice to have
• Please read the attachment with all the detailed instructions

```html
<!DOCTYPE html>
<html lang="en">
<head>
<meta charset="UTF-8">
<title>VOLT – Monitoring Natural Hazards</title>
<link href="https://fonts.googleapis.com/css2?family=Space+Mono:wght@700&family=Jost:wght@400;500&display=swap" rel="stylesheet">
<style>
  :root {
    --teal: #27505a;
    --teal-deep: #1f4149;
    --gold: #eeb937;
    --earth-blue: #6d93b4;
    --cloud: #d9e2ea;
    --panel-dark: #0f1416;
    --white: #ffffff;
  }
  * { margin: 0; padding: 0; box-sizing: border-box; }
  html, body { width: 1200px; height: 675px; overflow: hidden; }
  body { position: relative; background: var(--teal-deep); font-family: "Jost", sans-serif; color: var(--white); }

  .hero-backdrop {
    position: absolute; inset: 0;
    background:
      linear-gradient(180deg, rgba(0,0,0,0) 0%, rgba(0,0,0,0) 42%, rgba(109,147,180,0.55) 60%, rgba(190,208,222,0.75) 80%, rgba(150,170,190,0.7) 100%),
      linear-gradient(90deg, var(--teal-deep) 0%, var(--teal) 30%, #8c8a4c 52%, #d8b13d 68%, var(--gold) 100%);
  }

  .feature-panel {
    position: absolute; left: 374px; top: 82px; width: 451px; height: 535px;
    background:
      radial-gradient(ellipse at 60% 40%, rgba(70,70,60,0.55) 0%, rgba(20,24,26,0) 60%),
      linear-gradient(180deg, #1c1e1c 0%, #2a2b27 35%, #2b3438 60%, var(--panel-dark) 100%);
  }

  .brand {
    position: absolute; left: 0; right: 0; top: 136px;
    display: flex; flex-direction: column; align-items: center; gap: 10px;
  }
  .brand-mark { width: 60px; height: 60px; border: 2px solid var(--white); border-radius: 50%; }
  .brand-name { font-family: "Jost", sans-serif; font-weight: 500; font-size: 26px; letter-spacing: 8px; line-height: 1; padding-left: 8px; }

  .headline {
    position: absolute; left: 0; right: 0; top: 266px;
    font-family: "Space Mono", monospace; font-weight: 700;
    font-size: 51px; line-height: 56px; letter-spacing: 2.6px;
    text-align: center; text-transform: uppercase; white-space: nowrap;
  }

  .divider { position: absolute; left: 487px; top: 404px; width: 226px; height: 2px; background: var(--white); }

  .intro {
    position: absolute; left: 392px; width: 416px; top: 438px;
    font-size: 11.6px; line-height: 13.5px; text-align: center;
  }

  .actions { position: absolute; top: 537px; left: 464px; display: flex; gap: 32px; }
  .btn {
    width: 120px; height: 37px; border: 2px solid var(--white);
    display: flex; align-items: center; justify-content: center;
    font-family: "Space Mono", monospace; font-weight: 700; font-size: 14px; letter-spacing: 0.5px;
    color: var(--white); text-decoration: none;
  }
  .btn-register { background: linear-gradient(90deg, #e9eef0 0%, #5b7c80 35%, var(--teal) 60%, #8d8f48 100%); }
  .btn-login { background: transparent; }
</style>
</head>
<body>
  <div class="hero-backdrop" role="img" aria-label="Photo of Earth seen from orbit with cloud cover, tinted from teal to golden yellow"></div>
  <div class="feature-panel" role="img" aria-label="Photo of a satellite with solar panels orbiting above Earth"></div>

  <div class="brand">
    <span class="brand-mark"></span>
    <span class="brand-name">VOLT</span>
  </div>

  <h1 class="headline">Monitoring natural hazards in<br>humanitarian camps around the world</h1>

  <div class="divider"></div>

  <p class="intro">We simplify satellite image processing by removing the complexity for our users. Our advanced technology handles all the behind-the-scenes data analysis, allowing you to focus on insights rather than the technical details. With seamless integration and intuitive results, we deliver the information you need quickly and efficiently—no expertise in satellite imagery required.</p>

  <div class="actions">
    <a class="btn btn-register" href="#">REGISTER</a>
    <a class="btn btn-login" href="#">LOGIN</a>
  </div>
</body>
</html>
```